Norwegian Mobile Home/Cabin Producer Needs Brochure Design

We make and deliver our own brand of mobile homes especially made for Norway and it's weather conditions. We differ from other brands in building quality in regards to a much more solid construction, insulation and choices. We work with our customer from the beginning and build them after their demands and wishes.
We need a brochure that holds us out as top of the line. We deliver mobile homes of all kinds and sizes. Both to the private and professional sector.
For the professional sector, mainly camping sites we want to show, lodges-, sanitary- and kitchen wagoons etc.
So we need a brochure of 14-20 pages in A4 where the double pages can be printed in A3 format.
We have logo (provided). But we need cover as well as back suggestions.
It should start with pages where we can teel who we are and stand for.Piicture(s) and space for some editable text (which we can write in norwegian). The text part can have a transparent background......or not. Give us your best shot. Also a smaller part in the private sector that shows winter time.
We want other pages for the private sector that shows what we deliver and the possibilities of choices.
Pages for the the professional sector.
Pages that show our production. How we transport. And the split construction. Only pictures from this portfolio here. (see skydrive portfolios)
Take a look at provided pictures and our website www.solvikvarde.no for inspiration.
Here's a SkyDrive link to Pictures to choose from. http://lnkbox.example/QK41TP
(Hope it Works, let me know if not)
Our company name in small letters "solvikvarde fritidshytter" means directly translated "sunbay cottage shelters".
Looking forward to your suggestions.
Target Market(s)
Private market for vacation mobile homes. Camping sites and similar
Industry/Entity Type
Insulation
Requirements
Must have
- Our logo on the front page. Simple but inviting and professional
Logo and address on the back.

```html
<!DOCTYPE html>
<html lang="en">
<head>
<meta charset="utf-8">
<title>Brochure Spread</title>
<link rel="stylesheet" href="https://fonts.googleapis.com/css2?family=Alike&family=Source+Sans+3:wght@400&display=swap">
<style>
  :root {
    --lime: #bed62f;
    --white: #ffffff;
    --body-text: #f3f3ee;
    --wall-light: #c9bfb6;
    --wall-mid: #a89d94;
    --floor: #5f5852;
    --floor-dark: #3c3733;
  }
  html, body {
    margin: 0;
    padding: 0;
    overflow: hidden;
    background: var(--white);
  }
  .spread {
    position: relative;
    width: 1200px;
    height: 842px;
    overflow: hidden;
    font-family: "Source Sans 3", sans-serif;
  }
  .panel-left {
    position: absolute;
    left: 0;
    top: 0;
    width: 599px;
    height: 842px;
    background: var(--lime);
  }
  .corner-tab {
    position: absolute;
    left: 0;
    top: 0;
    width: 53px;
    height: 98px;
    background: var(--white);
  }
  .spine-title {
    position: absolute;
    left: 58px;
    top: 28px;
    margin: 0;
    writing-mode: vertical-rl;
    font-family: "Alike", serif;
    font-weight: 400;
    font-size: 44px;
    line-height: 1;
    color: var(--white);
    letter-spacing: 0.5px;
  }
  .panel-right {
    position: absolute;
    left: 599px;
    top: 0;
    width: 601px;
    height: 842px;
  }
  .interior-photo {
    position: absolute;
    inset: 0;
    width: 100%;
    height: 100%;
  }
  .accent-block {
    position: absolute;
    left: 461px;
    top: 498px;
    width: 140px;
    height: 91px;
    background: var(--lime);
  }
  .feature {
    position: absolute;
    right: 49px;
    top: 640px;
    width: 520px;
    text-align: right;
  }
  .feature-title {
    margin: 0 0 8px;
    font-family: "Alike", serif;
    font-weight: 400;
    font-size: 48px;
    line-height: 1;
    color: var(--lime);
  }
  .feature-body {
    margin: 0;
    font-size: 10.5px;
    line-height: 12px;
    color: var(--body-text);
  }
</style>
</head>
<body>
<main class="spread">
  <section class="panel-left">
    <div class="corner-tab"></div>
    <h2 class="spine-title">Lorem Ipsum</h2>
  </section>

  <section class="panel-right">
    <svg class="interior-photo" viewBox="0 0 601 842" preserveAspectRatio="none" role="img" aria-label="Photo of a cabin interior: dark wooden bar table with two tall stools, a vase of yellow orchids, beige curtains, a wall-mounted TV and a grey wood-grain floor">
      <defs>
        <linearGradient id="room-tone" x1="0" y1="0" x2="0" y2="1">
          <stop offset="0" stop-color="var(--wall-light)"/>
          <stop offset="0.6" stop-color="var(--wall-mid)"/>
          <stop offset="0.72" stop-color="var(--floor)"/>
          <stop offset="1" stop-color="var(--floor-dark)"/>
        </linearGradient>
      </defs>
      <rect width="601" height="842" fill="url(#room-tone)"/>
    </svg>
    <div class="accent-block"></div>
    <article class="feature">
      <h1 class="feature-title">Lorem Ipsum Dolor</h1>
      <p class="feature-body">
        Lorem ipsum dolor sit amet, vis quem consul nullam te, qui aeterno aliquid eu.<br>
        Ex pri duis mediocrem explicari, vidit graecis albucius in nec. Per aperiam legendos<br>
        et, animal posidonium ex vix. Velit dicunt ut nec. An ridens facilisis elaboraret nec,<br>
        te platonem postulant abhorreant eum, at nam malis aliquid evertitur.<br>
        Eum ne noster conceptam disputando, audiam iuvaret eam ei.
      </p>
    </article>
  </section>
</main>
</body>
</html>
```